Satchel & Compass needs new business card design

I need a new business card design. I'm looking for out-of-the-box design which represents the freedom of being a location independent entrepreneur.
I offer coaching, retreats and trips.
I would like to see designs with and without the photo.
Colors I use are black (#000000), green (#25A796) and brown (#D7C38C)
Website satchelandcompass.com

Target Market(s)

location independent entrepreneurs, digital nomads, people looking to swap the 9 to 5 for a lifestyle business

Industry/Entity Type

Business

Contact Information for Business Card

Petra Varga
Your Lifestyle Business Coach, Retreat & Trip Leader
http://satchelandcompass.com
hello@satchelandcompass.com
Live a life you don't need a holiday from

Font styles to use
Serif
Sans Serif

Requirements
Must have
• One side should contain only the logo. I would also consider having the "Live a life you don't need a holiday from" on that side too (depending on how it looks)
• Please show both sides on the designs.

```html
<!DOCTYPE html>
<html lang="en">
<head>
<meta charset="utf-8">
<title>Satchel &amp; Compass – Business Card</title>
<link rel="stylesheet" href="https://fonts.googleapis.com/css2?family=Roboto+Condensed:wght@400;700&family=Dancing+Script:wght@600&display=swap">
<style>
  :root {
    --ink: #000000;
    --green: #25A796;
    --text: #222222;
    --paper: #ffffff;
    --backdrop: #e4e4e6;
    --photo-leaf: #a9b89a;
    --photo-light: #eef0e6;
    --photo-warm: #d9d2b4;
  }
  * { box-sizing: border-box; margin: 0; padding: 0; }
  html, body { width: 1200px; height: 800px; overflow: hidden; }
  body {
    background: var(--backdrop);
    font-family: "Roboto Condensed", Arial, sans-serif;
    color: var(--text);
    display: flex;
    align-items: center;
    justify-content: center;
    gap: 50px;
  }
  .card {
    position: relative;
    width: 525px;
    height: 300px;
    background: var(--paper);
    overflow: hidden;
    box-shadow: 0 6px 18px rgba(0,0,0,.12);
  }
  .card__band {
    position: absolute;
    left: 0; right: 0;
    bottom: 22px;
    height: 12px;
    background: var(--green);
  }
  .wordmark {
    font-family: "Roboto Condensed", Arial, sans-serif;
    font-weight: 700;
    text-transform: uppercase;
    color: var(--ink);
    letter-spacing: 1px;
    line-height: 1;
  }

  /* Logo side */
  .card--logo .wordmark {
    position: absolute;
    top: 110px; left: 0; right: 0;
    text-align: center;
    font-size: 40px;
  }
  .card--logo .tagline {
    position: absolute;
    top: 172px; left: 0; right: 0;
    text-align: center;
    font-size: 17px;
    color: var(--text);
  }

  /* Photo side */
  .card__photo {
    position: absolute;
    inset: 0;
    background:
      linear-gradient(90deg, rgba(255,255,255,0) 0%, rgba(255,255,255,.35) 45%, rgba(255,255,255,.85) 75%, rgba(255,255,255,.95) 100%),
      radial-gradient(ellipse at 25% 45%, var(--photo-light) 0%, var(--photo-warm) 30%, var(--photo-leaf) 70%, #c9d1bf 100%);
  }
  .card--photo .wordmark {
    position: absolute;
    top: 62px; right: 26px;
    font-size: 34px;
    text-align: right;
  }
  .contact {
    position: absolute;
    right: 26px;
    top: 128px;
    text-align: right;
    font-size: 15px;
    line-height: 1.3;
    color: var(--text);
  }
  .contact__name {
    font-family: "Dancing Script", cursive;
    color: var(--green);
    font-size: 24px;
    line-height: 1.2;
  }
  .contact__rule {
    width: 200px;
    height: 1px;
    background: var(--green);
    margin: 5px 0 4px auto;
  }
  .card__links {
    position: absolute;
    left: 24px;
    bottom: 42px;
    font-size: 14px;
    color: var(--text);
  }
</style>
</head>
<body>
  <section class="card card--logo" aria-label="Business card, logo side">
    <div class="wordmark">Satchel &amp; Compass</div>
    <p class="tagline">Live a life you don't need a holiday from</p>
    <div class="card__band"></div>
  </section>

  <section class="card card--photo" aria-label="Business card, contact side">
    <div class="card__photo" role="img" aria-label="Faded outdoor photo of the coach standing among trees holding a small sign"></div>
    <div class="wordmark">Satchel &amp; Compass</div>
    <div class="contact">
      <p class="contact__name">Petra Varga</p>
      <p>Your Lifestyle Business Coach</p>
      <p>Retreat &amp; Trip Leader</p>
      <div class="contact__rule"></div>
      <p>satchelandcompass.com</p>
    </div>
    <p class="card__links">www.satchelandcompass.com &nbsp;|&nbsp; hello@satchelandcompass.com</p>
    <div class="card__band"></div>
  </section>
</body>
</html>
```